Sign Shop website

We need a web design for a sign company called Quillby Signs that builds signs for shops such as A Frames, Banners, Tennet Boards, Shop front windows etc...

The existing site is avaliable at www.quillbysigns.com.au

We will need to have a fresh makeover. The new site must have the following:

Photo Galleries (broken down into sections)
Store Locations (currently there are 4 stores)
Online quote form
List of services
About Us Page

We just need to front page designed in photoshop (the inner page is not necessary) We have a team that can code the site up.

The website should have the exact logo. Any person who alters the logo, design will be elimated.

No Twitter, RSS, LinkedIn icons

The main colours are yellow, black, blue, red

Target Market(s)

Any business

Industry/Entity Type

It Company

Requirements
Must have
• jQuery slider banner
Should not have
• Alter the logo in any way

```html
<!DOCTYPE html>
<html lang="en">
<head>
<meta charset="utf-8">
<title>Quillby Signs &amp; Digital Printing</title>
<link href="https://fonts.googleapis.com/css2?family=Bebas+Neue&family=Arimo:wght@400;700&display=swap" rel="stylesheet">
<style>
  :root {
    --red: #c8372f;
    --red-dark: #9e2620;
    --red-deep: #7a1c17;
    --yellow: #f0c628;
    --yellow-dark: #c99a14;
    --ink: #111111;
    --white: #ffffff;
    --heading-red: #c0302a;
    --field-text: #8a6a10;
  }
  * { margin: 0; padding: 0; box-sizing: border-box; }
  html, body { width: 1200px; height: 923px; overflow: hidden; }
  body {
    position: relative;
    font-family: "Arimo", Arial, sans-serif;
    background:
      repeating-linear-gradient(90deg, rgba(0,0,0,0.035) 0 2px, transparent 2px 38px),
      linear-gradient(180deg, #c9392f 0%, #c23a30 50%, #c53a31 100%);
    color: var(--ink);
  }
  .display { font-family: "Bebas Neue", Impact, sans-serif; font-weight: 400; }

  .top-contacts {
    position: absolute; top: 8px; right: 140px;
    display: flex; align-items: center; gap: 10px;
    color: #f6dcd6; font-size: 15px;
  }
  .top-contacts .divider { width: 1px; height: 20px; background: rgba(255,255,255,0.35); }
  .top-contacts svg { width: 14px; height: 16px; margin-right: 4px; vertical-align: -2px; }

  .site-header {
    position: absolute; left: 138px; top: 38px; width: 924px; height: 91px;
    background: linear-gradient(180deg, #f3d23a, #e9bf1f);
    border: 4px solid var(--yellow-dark);
    box-shadow: 0 3px 6px rgba(0,0,0,0.3);
  }
  .brand {
    position: absolute; left: 20px; top: 20px;
    display: flex; align-items: center; gap: 10px;
    font-family: "Bebas Neue", Impact, sans-serif; font-size: 44px; color: var(--red-deep);
  }
  .brand .mark { width: 24px; height: 24px; background: var(--red-deep); }
  .main-nav { position: absolute; right: 20px; top: 33px; display: flex; }
  .main-nav a {
    font-family: "Bebas Neue", Impact, sans-serif; font-size: 23px;
    color: var(--heading-red); text-decoration: none; padding: 0 8px;
    border-left: 1px solid rgba(160,80,20,0.45); line-height: 23px;
  }
  .main-nav a:first-child { border-left: none; }
  .main-nav a.current { color: var(--ink); }

  .hero-title {
    position: absolute; left: 162px; top: 188px;
    font-size: 40px; color: var(--yellow); letter-spacing: 0.3px;
    text-shadow: 0 2px 3px rgba(0,0,0,0.35);
  }
  .hero-text {
    position: absolute; left: 165px; top: 245px; width: 480px;
    font-size: 13px; line-height: 20.5px; color: #fbe9e5; text-align: justify;
  }
  .hero-media {
    position: absolute; left: 690px; top: 138px; width: 375px; height: 285px;
    background: linear-gradient(135deg, #eeeeee, #c9c9c9 50%, #e4e4e4);
    transform: rotate(-4deg);
    box-shadow: 0 6px 14px rgba(0,0,0,0.35);
  }
  .slider-arrow { position: absolute; top: 222px; width: 38px; height: 70px; }
  .slider-arrow.prev { left: 78px; }
  .slider-arrow.next { left: 1089px; }

  .content-panel {
    position: absolute; left: 140px; top: 426px; width: 922px; height: 398px;
    background: var(--white); box-shadow: 0 2px 6px rgba(0,0,0,0.3);
  }
  .welcome-title {
    position: absolute; left: 15px; top: 20px;
    font-size: 35px; color: var(--heading-red); letter-spacing: -0.2px;
  }
  .welcome-text {
    position: absolute; left: 16px; top: 68px; width: 596px;
    font-size: 13px; line-height: 20.6px; hyphens: auto;
  }
  .gallery-title {
    position: absolute; left: 16px; top: 170px; font-size: 32px; color: var(--ink);
  }
  .gallery-rule { position: absolute; left: 16px; top: 210px; width: 602px; height: 1px; background: #999; }
  .gallery-nav { position: absolute; left: 593px; top: 186px; width: 28px; height: 16px; }
  .gallery-row { position: absolute; left: 18px; top: 211px; display: flex; gap: 12px; }
  .gallery-tag { position: relative; width: 141px; height: 162px; }
  .gallery-tag svg.frame { position: absolute; inset: 0; }
  .gallery-tag .photo {
    position: absolute; left: 7px; top: 57px; width: 127px; height: 97px;
    border: 3px solid #fff;
  }
  .photo.car-white { background: linear-gradient(160deg, #d8d8d8, #8f9090 60%, #5d5e5e); }
  .photo.ute { background: linear-gradient(170deg, #b9a678, #e4e4e4 50%, #7d7d7d); }
  .photo.panels-logo { background: linear-gradient(180deg, #ffffff, #e7edf6 70%, #f4f4f4); }
  .photo.danger-sign { background: linear-gradient(180deg, #d92420 0 30%, #ffffff 30% 100%); }

  .quote-box { position: absolute; left: 783px; top: 454px; width: 266px; height: 342px; }
  .quote-box svg.envelope { position: absolute; inset: 0; }
  .quote-title {
    position: absolute; left: 28px; top: 13px; font-size: 38px; color: #4a3a0c;
    letter-spacing: -0.2px; word-spacing: -3px;
  }
  .field {
    position: absolute; left: 30px; width: 203px; height: 30px;
    background: #fbfbf4; border: 1px solid #c99a14; border-radius: 3px;
    display: flex; align-items: center; font-size: 13.5px; color: var(--field-text);
  }
  .field .icon {
    width: 26px; height: 100%; border-right: 1px solid #e0cf93;
    display: flex; align-items: center; justify-content: center; margin-right: 9px;
  }
  .field .icon svg { width: 14px; height: 14px; }
  .submit {
    position: absolute; left: 31px; top: 189px; width: 202px; height: 42px;
    background: linear-gradient(180deg, #dc4a40, #b92f27);
    border: 1px solid #8d201b; border-radius: 2px;
    color: #5b140f; font-size: 32px; text-align: center; line-height: 44px;
  }

  .footer-nav { position: absolute; left: 140px; top: 849px; display: flex; }
  .footer-nav a {
    font-family: "Bebas Neue", Impact, sans-serif; font-size: 22px; color: var(--ink);
    text-decoration: none; padding: 0 6px; border-left: 1px solid rgba(0,0,0,0.5); line-height: 21px;
  }
  .footer-nav a:first-child { padding-left: 0; border-left: none; }
  .copyright { position: absolute; left: 140px; top: 880px; font-size: 13.5px; color: var(--ink); }
  .copyright span { color: #f7dcd7; }
  .owned-badge { position: absolute; left: 992px; top: 834px; width: 64px; height: 64px; background: #2a1614; opacity: 0.7; }
</style>
</head>
<body>

<div class="top-contacts">
  <svg viewBox="0 0 14 16"><path d="M3 1 L6 1 L7 5 L5 6 Q6 10 9 11 L10 9 L13 10 L13 13 Q11 15 8 14 Q2 11 1 4 Q1 2 3 1 Z" fill="#f5c21d"/></svg>
  <span>Harwick (08) 5550 1234</span>
  <span class="divider"></span>
  <span>Brenmoor (08) 5550 6789</span>
</div>

<header class="site-header">
  <div class="brand"><span class="mark"></span>Quillby Signs</div>
  <nav class="main-nav">
    <a class="current" href="#">Home</a>
    <a href="#">Abouts Us</a>
    <a href="#">Our Services</a>
    <a href="#">Store Locations</a>
    <a href="#">Contact Us</a>
  </nav>
</header>

<svg class="slider-arrow prev" viewBox="0 0 38 70"><polyline points="36,2 2,35 36,68" fill="none" stroke="rgba(255,255,255,0.55)" stroke-width="2"/></svg>
<svg class="slider-arrow next" viewBox="0 0 38 70"><polyline points="2,2 36,35 2,68" fill="none" stroke="rgba(255,255,255,0.55)" stroke-width="2"/></svg>

<h1 class="hero-title display">Lorem Ipsum is simply dummy text</h1>
<p class="hero-text">Lorem Ipsum is simply dummy text of the printing and typesetting industry. Lorem Ipsum has been the industry's standard dummy text ever since the 1500s, when an unknown printer took a galley of type and scrambled it to make a type specimen book. It has survived not only five centuries, but also the leap into electronic typesetting, remaining essentially unchanged. It was popularised in the 1960s with the release of Letraset sheets containing Lorem Ipsum</p>
<div class="hero-media" role="img" aria-label="Fanned stack of printed sign samples: warning, danger and vehicle signs"></div>

<main class="content-panel">
  <h2 class="welcome-title display">Welcome to Quillby Signs &amp; Digital Printing</h2>
  <p class="welcome-text">Quillby Signs is a West Australian owned and managed company. We manufacture signage for any application; vinyl lettering, pull up banners, vehicle signage, in fact anything that requires our customers seeing the full picture when it comes to advertising their business. So if you're serious about the best, put us to the test!</p>

  <h3 class="gallery-title display">Photo Galleries</h3>
  <svg class="gallery-nav" viewBox="0 0 28 16"><polyline points="10,1 3,8 10,15" fill="none" stroke="#333" stroke-width="2.5"/><polyline points="18,1 25,8 18,15" fill="none" stroke="#333" stroke-width="2.5"/></svg>
  <div class="gallery-rule"></div>

  <div class="gallery-row">
    <figure class="gallery-tag">
      <svg class="frame" viewBox="0 0 141 162"><path d="M60 0 Q70 8 70 18" fill="none" stroke="#777" stroke-width="1.5"/><path d="M70 14 L141 38 L141 162 L0 162 L0 38 Z" fill="#000"/><circle cx="70" cy="28" r="4" fill="#fff"/></svg>
      <div class="photo car-white" role="img" aria-label="Rear of a white car with printed vehicle signage"></div>
    </figure>
    <figure class="gallery-tag">
      <svg class="frame" viewBox="0 0 141 162"><path d="M60 0 Q70 8 70 18" fill="none" stroke="#777" stroke-width="1.5"/><path d="M70 14 L141 38 L141 162 L0 162 L0 38 Z" fill="#000"/><circle cx="70" cy="28" r="4" fill="#fff"/></svg>
      <div class="photo ute" role="img" aria-label="Tailgate of a white utility vehicle with lettering"></div>
    </figure>
    <figure class="gallery-tag">
      <svg class="frame" viewBox="0 0 141 162"><path d="M60 0 Q70 8 70 18" fill="none" stroke="#777" stroke-width="1.5"/><path d="M70 14 L141 38 L141 162 L0 162 L0 38 Z" fill="#000"/><circle cx="70" cy="28" r="4" fill="#fff"/></svg>
      <div class="photo panels-logo" role="img" aria-label="Printed business sign for a panel company"></div>
    </figure>
    <figure class="gallery-tag">
      <svg class="frame" viewBox="0 0 141 162"><path d="M60 0 Q70 8 70 18" fill="none" stroke="#777" stroke-width="1.5"/><path d="M70 14 L141 38 L141 162 L0 162 L0 38 Z" fill="#000"/><circle cx="70" cy="28" r="4" fill="#fff"/></svg>
      <div class="photo danger-sign" role="img" aria-label="Danger safety sign, sewer pressure main below"></div>
    </figure>
  </div>
</main>

<aside class="quote-box">
  <svg class="envelope" viewBox="0 0 266 342">
    <defs>
      <linearGradient id="pocket-yellow" x1="0" y1="0" x2="0" y2="1">
        <stop offset="0" stop-color="#e9b91c"/>
        <stop offset="0.5" stop-color="#f0c62a"/>
        <stop offset="1" stop-color="#e0ad17"/>
      </linearGradient>
      <linearGradient id="envelope-red" x1="0" y1="0" x2="0" y2="1">
        <stop offset="0" stop-color="#d2463c"/>
        <stop offset="1" stop-color="#bd3229"/>
      </linearGradient>
    </defs>
    <rect x="8.5" y="0.5" width="241" height="240" rx="3" fill="#fff" stroke="#e2e2e2"/>
    <rect x="0" y="210" width="266" height="132" rx="6" fill="#a9271f"/>
    <rect x="16" y="9" width="232" height="280" fill="url(#pocket-yellow)"/>
    <line x1="16" y1="60" x2="248" y2="60" stroke="#d6a818"/>
    <path d="M0 214 L133 278 L266 214 L266 336 Q266 342 260 342 L6 342 Q0 342 0 336 Z" fill="url(#envelope-red)"/>
    <path d="M0 214 L133 278 L266 214" fill="none" stroke="#e8695e" stroke-width="1"/>
    <path d="M10 334 L133 282 L256 334" fill="none" stroke="#8a1f19" stroke-width="1.5"/>
  </svg>
  <h3 class="quote-title display">Get a free quote</h3>
  <div class="field" style="top:76px">
    <span class="icon"><svg viewBox="0 0 14 14"><circle cx="7" cy="4" r="3" fill="#b58a12"/><path d="M1 14 Q1 8 7 8 Q13 8 13 14 Z" fill="#b58a12"/></svg></span>Name
  </div>
  <div class="field" style="top:113px">
    <span class="icon"><svg viewBox="0 0 14 14"><rect x="1" y="3" width="12" height="8" fill="#b58a12"/><polyline points="1,3 7,8 13,3" fill="none" stroke="#fff3c0" stroke-width="1"/></svg></span>Email
  </div>
  <div class="field" style="top:150px">
    <span class="icon"><svg viewBox="0 0 14 14"><path d="M3 1 L5 1 L6 4 L4.5 5 Q5.5 8 8 9 L9 7.5 L12 8.5 L12 11 Q10 13 7 12 Q2 9.5 1.5 3.5 Q1.5 1.5 3 1 Z" fill="#b58a12"/></svg></span>Phone
  </div>
  <div class="submit display">Submit</div>
</aside>

<nav class="footer-nav">
  <a href="#">Home</a>
  <a href="#">Abouts Us</a>
  <a href="#">Our Services</a>
  <a href="#">Store Locations</a>
  <a href="#">Contact Us</a>
</nav>
<p class="copyright">Copyright © <span>Quillby Signs &amp; Digital Printing</span></p>
<div class="owned-badge" aria-hidden="true"></div>

</body>
</html>
```